Need Modern Elegant Professional Invoice Design

Need modern elegant professional invoice design along with a second page for time and expense log for professional services

```html
<!DOCTYPE html>
<html lang="en">
<head>
<meta charset="UTF-8">
<title>Invoice</title>
<link href="https://fonts.googleapis.com/css2?family=Anton&family=Lato:wght@400;700;900&display=swap" rel="stylesheet">
<style>
  :root {
    --orange: #ec7a2c;
    --ink: #2b2b2b;
    --text: #444444;
    --grey-head: #b3b3b3;
    --grey-row: #ededed;
    --rule: #d6d6d6;
    --paper: #ffffff;
    --backdrop: #e9e9e9;
  }
  * { margin: 0; padding: 0; box-sizing: border-box; }
  html, body { width: 1200px; height: 960px; overflow: hidden; }
  body {
    background: var(--backdrop);
    font-family: "Lato", sans-serif;
    color: var(--text);
    position: relative;
  }
  .invoice-page {
    position: absolute;
    left: 280px; top: 30px;
    width: 640px; height: 900px;
    background: var(--paper);
    box-shadow: 0 10px 30px rgba(0,0,0,0.12);
  }
  .brand {
    position: absolute; left: 44px; top: 66px;
    display: flex; align-items: center; gap: 8px;
    font-weight: 900; font-size: 22px; line-height: 26px; color: var(--orange);
    letter-spacing: 0.5px;
  }
  .brand-dot { width: 14px; height: 14px; border-radius: 50%; background: var(--orange); }
  .band-left {
    position: absolute; left: 0; top: 118px; width: 388px; height: 20px;
    background: var(--orange);
  }
  .band-right {
    position: absolute; left: 548px; top: 96px; width: 92px; height: 22px;
    background: var(--orange);
  }
  .title {
    position: absolute; left: 398px; top: 96px;
    font-family: "Anton", sans-serif; font-weight: 400; font-size: 38px; line-height: 42px;
    color: var(--ink); letter-spacing: 1px;
  }
  .bill-to { position: absolute; left: 92px; top: 170px; }
  .bill-to h2 { font-size: 18px; line-height: 22px; font-weight: 900; color: var(--ink); }
  .bill-to .client { font-size: 14px; line-height: 18px; font-weight: 700; color: var(--ink); margin-top: 2px; }
  .bill-to .address { font-size: 12px; line-height: 16px; margin-top: 2px; }
  .meta {
    position: absolute; left: 400px; top: 168px;
    display: grid; grid-template-columns: 80px 110px; row-gap: 2px;
    font-size: 13px; line-height: 17px; color: var(--ink);
  }
  .meta .label { font-weight: 700; }
  .meta .value { text-align: right; }
  .items {
    position: absolute; left: 90px; top: 250px; width: 520px;
    border-collapse: collapse; font-size: 12px;
  }
  .items th {
    background: var(--grey-head); color: #fff; font-weight: 700;
    text-align: left; padding: 4px 8px; font-size: 12px; line-height: 14px;
  }
  .items td {
    height: 28px; padding: 0 8px; color: var(--ink);
    border-right: 1px solid var(--rule);
  }
  .items td:last-child { border-right: 0; }
  .items tbody tr:nth-child(odd) td { background: var(--grey-row); border-right-color: #fff; }
  .items .col-sr { width: 46px; }
  .items .col-desc { width: 214px; }
  .items .num { text-align: right; }
  .thanks {
    position: absolute; left: 110px; top: 418px; width: 250px;
    border-top: 1px solid var(--rule); padding-top: 8px;
    font-size: 13px; line-height: 16px; font-weight: 900; color: var(--ink);
  }
  .totals {
    position: absolute; left: 470px; top: 430px;
    display: grid; grid-template-columns: 62px 60px;
    font-size: 12px; line-height: 15px; font-weight: 700; color: var(--ink);
  }
  .total-box {
    position: absolute; left: 456px; top: 470px; width: 184px; height: 40px;
    background: var(--orange); color: #fff;
    font-size: 17px; font-weight: 700; letter-spacing: 0.5px;
    display: flex; align-items: center; padding-left: 18px;
  }
  .terms { position: absolute; left: 150px; top: 500px; font-size: 12px; line-height: 16px; }
  .terms h3, .payment h3 { font-size: 14px; line-height: 18px; font-weight: 900; color: var(--ink); margin-bottom: 2px; }
  .payment {
    position: absolute; left: 210px; top: 628px;
    font-size: 12px; line-height: 16px;
  }
  .payment-grid { display: grid; grid-template-columns: 110px 80px; }
  .footer-rule { position: absolute; height: 3px; background: var(--orange); }
  .footer-rule.sign { left: 560px; top: 766px; width: 80px; }
  .footer-rule.main { left: 0; top: 800px; width: 462px; }
  .sign-label {
    position: absolute; left: 470px; top: 776px;
    font-size: 13px; line-height: 16px; color: var(--ink);
  }
  .contact {
    position: absolute; left: 100px; top: 820px;
    display: flex; gap: 34px; font-size: 15px; line-height: 18px; font-weight: 900; color: var(--ink);
  }
  .contact .sep { font-weight: 400; color: var(--text); }
</style>
</head>
<body>
  <main class="invoice-page">
    <div class="brand"><span class="brand-dot"></span>Vantage Adjusters</div>

    <div class="band-left"></div>
    <h1 class="title">INVOICE</h1>
    <div class="band-right"></div>

    <section class="bill-to">
      <h2>Invoice to:</h2>
      <p class="client">Mr. Daniel Hart</p>
      <p class="address">Address..........</p>
    </section>

    <section class="meta">
      <span class="label">Invoice#</span><span class="value">52341</span>
      <span class="label">Date:</span><span class="value">01 / 03 / 2021</span>
    </section>

    <table class="items">
      <thead>
        <tr>
          <th class="col-sr">Sr.</th>
          <th class="col-desc">Item Description</th>
          <th>Price</th>
          <th>Qty.</th>
          <th>Total</th>
        </tr>
      </thead>
      <tbody>
        <tr><td>1.</td><td>Items.....</td><td class="num">500</td><td class="num">2</td><td class="num">1000</td></tr>
        <tr><td></td><td></td><td></td><td></td><td></td></tr>
        <tr><td></td><td></td><td></td><td></td><td></td></tr>
        <tr><td></td><td></td><td></td><td></td><td></td></tr>
        <tr><td></td><td></td><td></td><td></td><td></td></tr>
      </tbody>
    </table>

    <p class="thanks">Thanks, You for your Business</p>

    <div class="totals">
      <span>Sub total:</span><span>1000</span>
      <span>Tax:</span><span>0.5%</span>
    </div>
    <div class="total-box">TOTAL: 1000</div>

    <section class="terms">
      <h3>Terms &amp; Condition</h3>
      <p>Sample texct Sample texct</p>
      <p>Sample texct Sample texct</p>
      <p>Sample texct Sample texct</p>
      <p>Sample texct Sample texct</p>
      <p>Sample texct</p>
    </section>

    <section class="payment">
      <h3>Payment Info:</h3>
      <div class="payment-grid">
        <span>Account#</span><span>000000</span>
        <span>Account Name:</span><span>(Name)</span>
        <span>Bank Details:</span><span>(Bank)</span>
      </div>
    </section>

    <div class="footer-rule sign"></div>
    <p class="sign-label">Authorized Sign</p>
    <div class="footer-rule main"></div>

    <footer class="contact">
      <span>Phone</span><span class="sep">|</span>
      <span>Address</span><span class="sep">|</span>
      <span>Website</span>
    </footer>
  </main>
</body>
</html>
```